[WEB DESIGN - Start-up] Online LOANS against Luxury Assets - Needs a Web Design

Hello,
We need a web design for a new company. We make online LOANS against Luxury assets.
The name is private, that's why you could remplace it by the term "LOGO" or "MAISON PRÊT".

In attachments, you'll find few models that we would like. Nonetheless, we don't want a copy of these screenshots. They are only prototypes that we made. Here we expect you to lead a professional web Design with your intuition and your ideas.

The final design should communicate start-up spirit, professionalism and fluidity.

Best Regards.

Industry/Entity Type

Finance

Number of Pages Required

2 page

Font styles to use
Sans Serif

Colors
f78f20
ffffff
b2b2b2
e9e9e9

Requirements
Must have
• The designer will draw on the 2015 web trends.
• The subject site is serious (loans against luxury assets), but the site should be modern and pleasant.
• PLEASE REFER YOU TO MY MODEL ( ATTACHMENTS)
Nice to have
• Surprise-me ! Welcome to a lot of imagination.

```html
<!DOCTYPE html>
<html lang="fr">
<head>
<meta charset="utf-8">
<title>Maison Prêt – Prêt sur biens de luxe</title>
<link href="https://fonts.googleapis.com/css2?family=Open+Sans:wght@300;400;600;700&display=swap" rel="stylesheet">
<style>
:root{
  --orange:#f78f20;
  --white:#ffffff;
  --grey:#b2b2b2;
  --light:#e9e9e9;
  --text:#555555;
  --muted:#777777;
  --dark:#333333;
  --footer:#8c8c8c;
  --footer-dark:#6e6e6e;
}
*{box-sizing:border-box;margin:0;padding:0}
html,body{width:774px;height:1200px;overflow:hidden}
body{position:relative;font-family:"Open Sans",Arial,sans-serif;color:var(--text);background:var(--white);font-size:8px;line-height:1.4}

.site-header{height:56px;display:flex;align-items:center;justify-content:space-between;padding:0 36px 0 40px;background:var(--white)}
.brand{display:flex;align-items:center;gap:7px;font-weight:700;font-size:15px;color:var(--orange);letter-spacing:.5px}
.brand-mark{width:12px;height:12px;background:var(--orange)}
.main-nav{display:flex;gap:6px}
.main-nav a{font-size:8px;font-weight:700;color:var(--dark);text-decoration:none;padding:6px 9px;text-transform:uppercase}
.main-nav a.active{background:var(--orange);color:var(--white);border-radius:2px}

.hero{position:relative;height:254px;background:linear-gradient(120deg,#6e5a48 0%,#b08a62 30%,#e6d8c4 55%,#a88560 78%,#5d4a3a 100%)}
.hero-title{position:absolute;top:40px;width:100%;text-align:center;color:var(--orange);font-size:21px;font-weight:600;text-shadow:0 1px 2px rgba(0,0,0,.3)}
.quote-form{position:absolute;left:272px;top:88px;width:230px;height:112px;background:rgba(255,255,255,.88);border-radius:3px;padding:12px 14px}
.quote-form label{display:block;font-size:7px;color:var(--orange);margin-bottom:5px}
.form-row{display:flex;gap:8px;margin-bottom:6px}
.field{flex:1;height:15px;background:var(--white);border:1px solid var(--light);font-size:6.5px;color:#888;padding:3px 5px;display:flex;justify-content:space-between}
.field::after{content:"▾";color:var(--orange)}
.field.plain::after{content:""}
.form-btn{display:block;margin-top:10px;height:17px;background:var(--orange);color:var(--white);text-align:center;font-size:7.5px;font-weight:700;line-height:17px;border-radius:2px}

.steps{display:flex;gap:8px;padding:16px 40px 0}
.step{flex:1;border:1px solid var(--orange);border-radius:3px;height:96px;padding:8px 10px}
.step-head{display:flex;align-items:center;gap:8px;border-bottom:1px solid var(--light);padding-bottom:5px;margin-bottom:6px}
.step-num{font-size:7px;color:var(--orange)}
.step-name{font-size:12px;font-weight:600;color:var(--dark)}
.step p{font-size:6.5px;color:var(--muted)}

.products{padding:16px 40px 0}
.section-bar{display:flex;justify-content:space-between;align-items:center;border-bottom:1px solid var(--light);padding-bottom:5px}
.section-label{font-size:8px;font-weight:700;color:var(--dark)}
.arrows{display:flex;gap:3px}
.arrows span{width:14px;height:14px;background:var(--orange);color:var(--white);font-size:9px;text-align:center;line-height:14px;border-radius:2px}
.filters{display:flex;gap:3px;margin:6px 0 14px}
.filters span{background:var(--light);font-size:5.5px;padding:3px 7px;color:#888}
.filters span.on{background:var(--orange);color:var(--white)}
.product-grid{display:flex;gap:14px}
.product{flex:1}
.product-img{height:110px;border:1px solid var(--light)}
.product h4{font-size:7px;font-weight:600;color:var(--dark);margin-top:5px;text-transform:uppercase}
.img-instrument{background:linear-gradient(135deg,#c9c2b6,#6a5f55)}
.img-sculpture{background:linear-gradient(135deg,#f2ede2,#c59a3d 60%,#8a6a2b)}
.img-painting{background:linear-gradient(135deg,#d9c497,#a7875a 50%,#5e4a31)}
.img-vehicle{background:linear-gradient(160deg,#d8d8dc,#6b6e74 60%,#2e3035)}

.help{padding-top:24px;text-align:center}
.help h2{font-size:14px;font-weight:400;color:#888;letter-spacing:.5px}
.help-grid{display:flex;justify-content:center;gap:40px;margin-top:18px}
.help-box{width:132px;height:90px;background:var(--light);border:1px solid var(--grey);display:flex;flex-direction:column;align-items:center;justify-content:center;gap:6px;font-size:6.5px;color:var(--muted)}
.help-box strong{color:var(--dark);font-size:8px}

.tagline{margin-top:26px;border-top:1px solid var(--orange);border-bottom:1px solid var(--orange);text-align:center;padding:7px 0;color:var(--orange);font-size:12px}

.proof{display:flex;gap:18px;padding:14px 40px 0;height:124px}
.testimonials{width:240px}
.block-title{font-size:9px;font-weight:700;color:var(--dark);text-transform:uppercase;margin-bottom:8px}
.block-title.split{display:flex;justify-content:space-between;align-items:center}
.testimonial{border:1px solid var(--orange);padding:6px 8px;font-size:6.5px;color:var(--muted);margin-bottom:8px}
.author{display:flex;gap:8px;align-items:center;font-size:6.5px;color:var(--muted)}
.avatar{width:24px;height:24px;border-radius:50%;background:var(--grey);flex:none}
.figures{width:200px}
.counter{display:flex;gap:2px;margin-bottom:10px}
.counter span{width:20px;height:26px;background:var(--dark);color:var(--white);font-size:16px;font-weight:700;text-align:center;line-height:26px;border-radius:2px}
.proof-text{flex:1;font-size:6.5px;color:var(--muted);padding-top:20px}
.proof-text p{margin-bottom:8px}

.site-footer{position:absolute;top:975px;left:0;width:774px;height:200px;background:var(--footer);color:var(--white);display:flex;gap:30px;padding:22px 40px}
.site-footer h5{font-size:10px;font-weight:600;margin-bottom:8px}
.site-footer p,.site-footer li{font-size:6.5px;color:#eee}
.footer-about{width:230px}
.footer-links{width:140px}
.footer-links ul{list-style:none}
.footer-links li{margin-bottom:2px}
.footer-contact{flex:1}
.footer-bottom{position:absolute;top:1175px;left:0;width:774px;height:25px;background:var(--footer-dark);color:#ddd;font-size:6.5px;display:flex;justify-content:space-between;align-items:center;padding:0 40px}
</style>
</head>
<body>

<header class="site-header">
  <div class="brand"><span class="brand-mark"></span>Maison Prêt</div>
  <nav class="main-nav">
    <a class="active" href="#">Accueil</a>
    <a href="#">Lots prêts</a>
    <a href="#">Estimation</a>
    <a href="#">FAQ</a>
    <a href="#">Nous contacter</a>
  </nav>
</header>

<section class="hero" role="img" aria-label="Photo de fond : instruments de musique en cuivre posés sur des partitions">
  <h1 class="hero-title">On se lasse de tout,sauf de l'argent</h1>
  <form class="quote-form">
    <label>Demande de prêt</label>
    <div class="form-row"><span class="field">Catégorie</span><span class="field plain">Valeur estimée</span></div>
    <div class="form-row"><span class="field">Durée</span><span class="field plain">Montant souhaité</span></div>
    <span class="form-btn">ESTIMER MON PRÊT</span>
  </form>
</section>

<section class="steps">
  <article class="step">
    <div class="step-head">
      <svg width="22" height="22" viewBox="0 0 22 22"><circle cx="9" cy="9" r="6" fill="none" stroke="#f78f20" stroke-width="2"/><path d="M13 13l6 6" stroke="#f78f20" stroke-width="2.5"/></svg>
      <div><div class="step-num">Step 01</div><div class="step-name">Estimation</div></div>
    </div>
    <p>Décrivez votre bien en quelques clics et recevez une estimation gratuite de sa valeur sous vingt-quatre heures.</p>
  </article>
  <article class="step">
    <div class="step-head">
      <svg width="22" height="22" viewBox="0 0 22 22"><rect x="2" y="5" width="18" height="12" rx="2" fill="none" stroke="#f78f20" stroke-width="2"/><path d="M2 9h18" stroke="#f78f20" stroke-width="2"/></svg>
      <div><div class="step-num">Step 02</div><div class="step-name">Paiement</div></div>
    </div>
    <p>Une fois l'offre acceptée, les fonds sont versés directement sur votre compte bancaire en toute rapidité.</p>
  </article>
  <article class="step">
    <div class="step-head">
      <svg width="22" height="22" viewBox="0 0 22 22"><rect x="4" y="10" width="14" height="10" rx="1" fill="#f78f20"/><path d="M7 10V7a4 4 0 018 0v3" fill="none" stroke="#f78f20" stroke-width="2"/></svg>
      <div><div class="step-num">Step 03</div><div class="step-name">Sécurisation</div></div>
    </div>
    <p>Votre bien est conservé dans un coffre assuré et surveillé pendant toute la durée de votre prêt.</p>
  </article>
  <article class="step">
    <div class="step-head">
      <svg width="22" height="22" viewBox="0 0 22 22"><path d="M4 11a7 7 0 0112-5M18 11a7 7 0 01-12 5" fill="none" stroke="#f78f20" stroke-width="2"/><path d="M16 2v4h-4M6 20v-4h4" fill="none" stroke="#f78f20" stroke-width="2"/></svg>
      <div><div class="step-num">Step 04</div><div class="step-name">Rachat</div></div>
    </div>
    <p>Remboursez le prêt à votre rythme et récupérez votre bien, intact, à la fin de la période choisie.</p>
  </article>
</section>

<section class="products">
  <div class="section-bar">
    <span class="section-label">NOS PRODUITS</span>
    <div class="arrows"><span>‹</span><span>›</span></div>
  </div>
  <div class="filters">
    <span class="on">TOUS</span><span>INSTRUMENTS</span><span>ART - TABLEAUX</span><span>ART - SCULPTURE</span><span>BIJOUX</span><span>MONTRES</span><span>VÉHICULES</span><span>MAROQUINERIE</span><span>VINS</span>
  </div>
  <div class="product-grid">
    <div class="product"><div class="product-img img-instrument" role="img" aria-label="Photo d'un instrument de musique"></div><h4>Instrument</h4></div>
    <div class="product"><div class="product-img img-sculpture" role="img" aria-label="Photo d'une paire de vases dorés"></div><h4>Art - Sculpture</h4></div>
    <div class="product"><div class="product-img img-painting" role="img" aria-label="Photo d'un tableau ancien"></div><h4>Art - Tableaux</h4></div>
    <div class="product"><div class="product-img img-vehicle" role="img" aria-label="Photo d'une voiture de luxe"></div><h4>Véhicules</h4></div>
  </div>
</section>

<section class="help">
  <h2>BESOIN D'AIDE? NOUS SOMMES A VOTRE ECOUTE</h2>
  <div class="help-grid">
    <div class="help-box">
      <svg width="30" height="30" viewBox="0 0 30 30"><path d="M8 4l5 5-3 3c2 4 4 6 8 8l3-3 5 5-4 4C13 25 5 17 4 8z" fill="#777"/></svg>
      <span>Du lundi au vendredi 9h à 19h</span><strong>01 23 45 67 89</strong>
    </div>
    <div class="help-box">
      <svg width="30" height="30" viewBox="0 0 30 30"><text x="15" y="25" text-anchor="middle" font-family="Open Sans, sans-serif" font-size="28" font-weight="700" fill="#777">?</text></svg>
      <strong>Questions Fréquentes</strong>
    </div>
    <div class="help-box">
      <svg width="32" height="24" viewBox="0 0 32 24"><rect x="1" y="1" width="30" height="22" fill="#777"/><path d="M1 1l15 12L31 1" fill="none" stroke="#e9e9e9" stroke-width="2"/></svg>
      <span>Formulaire de Contact</span><strong>contact@maison-pret.fr</strong>
    </div>
  </div>
</section>

<p class="tagline">Maison Prêt est n°1 de la vente avec facilité de rach at</p>

<section class="proof">
  <div class="testimonials">
    <div class="block-title split">DERNIERS TÉMOIGNAGES <span class="arrows"><span>‹</span><span>›</span></span></div>
    <div class="testimonial">« Service rapide et équipe à l'écoute, j'ai obtenu mon prêt en deux jours et récupéré mon tableau sans souci. »</div>
    <div class="author"><span class="avatar"></span><span>Claire D., Lyon — Prêt sur tableau, remboursé en six mois sans frais cachés.</span></div>
  </div>
  <div class="figures">
    <div class="block-title">QUELQUES CHIFFRES</div>
    <div class="counter"><span>0</span><span>3</span><span>5</span><span>0</span><span>9</span><span>2</span></div>
    <div class="counter"><span>0</span><span>5</span><span>9</span><span>0</span><span>6</span><span>5</span></div>
  </div>
  <div class="proof-text">
    <p>Clients accompagnés depuis notre création, avec un taux de satisfaction supérieur à quatre-vingt-quinze pour cent.</p>
    <p>Euros prêtés en moyenne chaque mois sur des biens de valeur, conservés en toute sécurité jusqu'au rachat.</p>
  </div>
</section>

<footer class="site-footer">
  <div class="footer-about">
    <h5>Vendez En Ligne, Un Rachater</h5>
    <p>Maison Prêt propose des prêts rapides garantis par vos biens de luxe. Notre équipe d'experts estime chaque objet avec soin et vous fait une offre claire, sans engagement. Vos biens restent assurés et protégés jusqu'à votre rachat. Simple, transparent et sûr.</p>
  </div>
  <nav class="footer-links">
    <h5>Liens</h5>
    <ul>
      <li>Accueil</li><li>Lots prêts</li><li>Estimation</li><li>Nos produits</li><li>FAQ</li><li>Mentions légales</li><li>Nous contacter</li>
    </ul>
  </nav>
  <div class="footer-contact">
    <h5>Contactez-Nous</h5>
    <p>12 rue des Lilas<br>75011 Paris<br>01 23 45 67 89<br>contact@maison-pret.fr</p>
  </div>
</footer>
<div class="footer-bottom"><span>© Copyright Maison Prêt 2015</span><span>Tous droits réservés</span></div>

</body>
</html>
```